Manifesto

I want a manifesto with the following five manifestos for our Not for Profit

- We are a For-purpose organisation
- Every service we offer is free
- Every product we sell funds our services
- Every financial transaction is transparent
- Our service is for the greater good
- Our purpose is always to serve the people
- We are a for purpose organisation

Its to go with this website logo/look/feel www.brightlantern.co.nz

Two attachments:

1. I quite like this look/feel of a manifesto (see attached), I want something clean, professional but I also quite like either Retro modern look feel also like a fresh, and uplifting as its for sick people coming to see us and our funds where anyone buys a product are used for helping those who are sick with healing......so needs something conveyed that is fresh, uplifing yet professional.
2. This attachment is how I wrote this down when inspired of how I wanted Bright Lantern to operate. This is our values chart. It has to say

Also check out our website for our logo, look etc.. it doesnt have to be the same but red somewhere would link back to logo. www.brightlantern.co.nz .

```html
<!DOCTYPE html>
<html lang="en">
<head>
<meta charset="utf-8">
<title>Bright Lantern Manifesto</title>
<link href="https://fonts.googleapis.com/css2?family=Chewy&display=swap" rel="stylesheet">
<style>
  :root {
    --ink: #111111;
    --red: #e3161b;
    --paper: #ffffff;
    --dove-light: #f6f6f6;
    --dove-shade: #e2e2e2;
  }
  html, body {
    margin: 0;
    padding: 0;
    width: 900px;
    height: 1200px;
    overflow: hidden;
    background: var(--paper);
  }
  .manifesto {
    position: relative;
    width: 900px;
    height: 1200px;
    overflow: hidden;
    background: var(--paper);
  }
  .dove-art {
    position: absolute;
    left: 330px;
    top: 340px;
    width: 290px;
    height: 400px;
    border-radius: 48% 52% 40% 60% / 40% 45% 55% 60%;
    background: radial-gradient(ellipse at 55% 45%, var(--dove-light), var(--dove-shade));
  }
  .artwork {
    position: absolute;
    inset: 0;
  }
  .artwork text {
    font-family: "Chewy", sans-serif;
  }
  .ink { fill: var(--ink); }
  .red { fill: var(--red); }
  .outline {
    fill: var(--paper);
    stroke: var(--ink);
    stroke-width: 2;
  }
  .brand-name {
    fill: var(--red);
    font-size: 14px;
  }
  .flow {
    fill: none;
    stroke: var(--ink);
    stroke-width: 3;
    stroke-linecap: round;
  }
  .arrow-tip { fill: var(--ink); }
  .bloom-red { fill: var(--red); }
  .bloom-ink { fill: var(--ink); }
</style>
</head>
<body>
<main class="manifesto">

  <div class="dove-art" role="img" aria-label="White dove in flight with outspread wings"></div>

  <svg class="artwork" width="900" height="1200" viewBox="0 0 900 1200" role="group" aria-label="Bright Lantern manifesto">
    <defs>
      <marker id="arrowhead" viewBox="0 0 10 10" refX="6" refY="5" markerWidth="7" markerHeight="7" orient="auto">
        <path class="arrow-tip" d="M0,0 L10,5 L0,10 z"/>
      </marker>
    </defs>

    <g class="flows">
      <path class="flow" d="M525,178 C470,185 330,170 312,188 C300,205 420,210 520,220 C600,230 650,245 700,245" marker-end="url(#arrowhead)"/>
      <path class="flow" d="M700,245 C790,235 860,180 838,125 C834,118 828,112 822,108" marker-end="url(#arrowhead)"/>
      <path class="flow" d="M815,350 C835,390 800,435 740,435 C680,435 670,405 705,398 C740,390 640,385 575,400" marker-end="url(#arrowhead)"/>
      <path class="flow" d="M270,600 C200,590 90,590 55,610 C25,630 60,640 95,610 C120,590 125,630 122,668" marker-end="url(#arrowhead)"/>
      <path class="flow" d="M560,605 C640,590 740,585 780,610 C793,620 795,635 792,648" marker-end="url(#arrowhead)"/>
      <path class="flow" d="M470,1105 C500,1060 505,1000 480,960 C455,925 415,945 425,985 C435,1015 445,900 440,838" marker-end="url(#arrowhead)"/>
    </g>

    <g class="blooms">
      <circle class="bloom-red" cx="410" cy="265" r="14"/>
      <circle class="bloom-ink" cx="100" cy="810" r="14"/>
      <circle class="bloom-red" cx="800" cy="912" r="14"/>
    </g>

    <g class="line-free">
      <text class="red" x="35" y="185" font-size="175" textLength="195" lengthAdjust="spacingAndGlyphs">Every</text>
      <text class="red" x="235" y="103" font-size="62" textLength="215" lengthAdjust="spacingAndGlyphs">service</text>
      <text class="ink" x="475" y="95" font-size="46" textLength="235" lengthAdjust="spacingAndGlyphs">we offer is</text>
      <text class="red" x="725" y="100" font-size="60" textLength="125" lengthAdjust="spacingAndGlyphs">Free</text>
    </g>

    <g class="line-funds">
      <text class="ink" x="238" y="160" font-size="58" textLength="200" lengthAdjust="spacingAndGlyphs">product</text>
      <text class="ink" x="447" y="150" font-size="26" textLength="42" lengthAdjust="spacingAndGlyphs">we</text>
      <text class="ink" x="505" y="155" font-size="42" textLength="80" lengthAdjust="spacingAndGlyphs">sell</text>
      <text class="red" x="600" y="165" font-size="60" textLength="160" lengthAdjust="spacingAndGlyphs">Funds</text>
      <text class="ink" x="570" y="230" font-size="52" textLength="275" lengthAdjust="spacingAndGlyphs">our services</text>
    </g>

    <g class="line-transparent">
      <text class="ink" x="62" y="285" font-size="66" textLength="306" lengthAdjust="spacingAndGlyphs">Financial</text>
      <text class="ink" x="443" y="303" font-size="60" textLength="55" lengthAdjust="spacingAndGlyphs">is</text>
      <text class="outline" x="522" y="305" font-size="62" textLength="333" lengthAdjust="spacingAndGlyphs">transparent</text>
      <text class="ink" x="110" y="370" font-size="72" textLength="360" lengthAdjust="spacingAndGlyphs">transaction</text>
    </g>

    <g class="line-purpose-org">
      <text class="red" x="65" y="500" font-size="120" textLength="160" lengthAdjust="spacingAndGlyphs">We</text>
      <text class="red" x="288" y="445" font-size="52" textLength="30" lengthAdjust="spacingAndGlyphs">a</text>
      <text class="red" x="322" y="505" font-size="62" textLength="123" lengthAdjust="spacingAndGlyphs">For</text>
      <text class="red" x="150" y="575" font-size="60" textLength="118" lengthAdjust="spacingAndGlyphs">are</text>
      <text class="red" x="545" y="500" font-size="88" textLength="305" lengthAdjust="spacingAndGlyphs">purpose</text>
      <text class="red" x="540" y="580" font-size="56" textLength="310" lengthAdjust="spacingAndGlyphs">organisation</text>
    </g>

    <g class="line-greater-good">
      <text class="ink" x="190" y="690" font-size="84" textLength="140" lengthAdjust="spacingAndGlyphs">Our</text>
      <text class="red" x="70" y="760" font-size="82" textLength="285" lengthAdjust="spacingAndGlyphs">Service</text>
      <text class="ink" x="190" y="840" font-size="66" textLength="45" lengthAdjust="spacingAndGlyphs">is</text>
      <text class="red" x="75" y="925" font-size="62" textLength="110" lengthAdjust="spacingAndGlyphs">For</text>
      <text class="ink" x="220" y="925" font-size="62" textLength="110" lengthAdjust="spacingAndGlyphs">the</text>
      <text class="ink" x="30" y="1058" font-size="140" textLength="450" lengthAdjust="spacingAndGlyphs">greater</text>
      <text class="red" x="165" y="1122" font-size="90" textLength="220" lengthAdjust="spacingAndGlyphs">good</text>
    </g>

    <g class="line-serve-people">
      <text class="ink" x="700" y="730" font-size="92" textLength="135" lengthAdjust="spacingAndGlyphs">Our</text>
      <text class="red" x="580" y="795" font-size="76" textLength="260" lengthAdjust="spacingAndGlyphs">purpose</text>
      <text class="ink" x="485" y="870" font-size="60" textLength="335" lengthAdjust="spacingAndGlyphs" transform="rotate(3 485 870)">is always to</text>
      <text class="red" x="535" y="975" font-size="66" textLength="185" lengthAdjust="spacingAndGlyphs">serve</text>
      <text class="ink" x="735" y="1005" font-size="66" textLength="115" lengthAdjust="spacingAndGlyphs">the</text>
      <text class="red" x="500" y="1100" font-size="120" textLength="355" lengthAdjust="spacingAndGlyphs">people</text>
    </g>

    <text class="brand-name" x="400" y="1122">Bright Lantern</text>
  </svg>

</main>
</body>
</html>
```